Design and typesetting a NEVB report (approx 8-10 A4 pages)

We are a UK based ideas and innovation agency working within the UK Social Housing sector.
We have a report that needs designing up into an A4 PDF document that should run to about 8-10 A4 pages.
Design-wise we are looking for something dynamic with a housing and tech design theme. The document text is attached in the Word file.
Please find attached our logo and branding guidelines for font and logo use. We would be looking to use the main NEVB purple along with some NEW dynamic complimentary colours used throughout the design.
The report needs to read easily and cleanly so can be spaced out accordingly.
There will be on additional page of text to add at the back which we can send over once the successful candidate has been chosen.
Any questions please ask!
Target Market(s)
UK Social Housing sector
Industry/Entity Type
Social
Font styles to use
Other font styles liked:
- Gill Sans for body and Avant Garde for title (as specified in the attached branding guidelines)
Requirements
Must have
- Dynamic feel, stylish, colourful.
- Lots of space around the text.
Nice to have
- A bit of striking design work around the text (in the report template design)
Should not have
- Cluttered feel and fussy design.

```html
<!DOCTYPE html>
<html lang="en">
<head>
<meta charset="utf-8">
<title>NEVB – Is Housing Really Ready to Go Digital?</title>
<link rel="stylesheet" href="https://fonts.googleapis.com/css2?family=Cabin:wght@400;700&family=Questrial&display=swap">
<style>
  :root {
    --brand-purple: #6b5fad;
    --lilac: #a59bcc;
    --peach: #f9b08e;
    --salmon: #f59f7f;
    --leaf: #a5d07c;
    --ink: #1a1a1a;
    --paper: #ffffff;
    --spine: #b9b9bd;
  }
  * { box-sizing: border-box; margin: 0; padding: 0; }
  html, body { width: 1200px; height: 1000px; overflow: hidden; background: var(--paper); }
  body { position: relative; font-family: "Cabin", sans-serif; color: var(--ink); }

  .page { position: absolute; }
  .cover { left: 0; top: 0; width: 595px; height: 1000px; }

  .brand { position: absolute; display: flex; align-items: center; color: var(--brand-purple); }
  .brand-mark { background: var(--brand-purple); flex: none; }
  .brand-name { font-family: "Cabin", sans-serif; font-weight: 700; letter-spacing: 2px; line-height: 1; }

  .cover .brand { left: 150px; top: 148px; gap: 50px; }
  .cover .brand-mark { width: 58px; height: 58px; }
  .cover .brand-name { font-size: 74px; }
  .tagline { position: absolute; left: 125px; top: 216px; font-family: "Questrial", sans-serif; font-size: 22px; color: var(--brand-purple); }

  .title-triangle { position: absolute; left: 58px; top: 297px; }
  .report-title {
    position: absolute; left: 58px; top: 347px; width: 460px; text-align: center;
    font-family: "Questrial", sans-serif; font-weight: 400; font-size: 24px; line-height: 27px; color: var(--brand-purple);
  }

  .intro { position: absolute; left: 178px; width: 214px; font-size: 10.5px; line-height: 15.2px; }
  .intro-1 { top: 521px; }
  .intro-2 { top: 687px; }

  .folio { position: absolute; font-size: 9px; }
  .cover .folio { left: 296px; top: 861px; }

  .spread { left: 595px; top: 80px; width: 600px; height: 840px; background: var(--lilac); border-left: 5px solid var(--spine); }
  .spread .brand { left: 62px; top: 57px; width: 124px; height: 31px; background: var(--paper); padding-left: 6px; gap: 8px; }
  .spread .brand-mark { width: 18px; height: 18px; }
  .spread .brand-name { font-size: 24px; }

  .section-banner { position: absolute; left: 62px; top: 103px; }
  .section-heading { position: absolute; left: 88px; top: 127px; font-size: 15px; font-weight: 700; }
  .section-lede { position: absolute; left: 88px; top: 162px; font-size: 10.5px; }

  .content-panel { position: absolute; left: 62px; top: 206px; width: 484px; height: 585px; background: var(--paper); }
  .failure-point {
    position: absolute; width: 200px; background: var(--leaf); padding: 0 2px;
    font-size: 10px; line-height: 14.8px; text-align: justify; hyphens: auto; -webkit-hyphens: auto;
  }
  .fp-1 { left: 25px; top: 25px; height: 255px; }
  .fp-3 { left: 250px; top: 25px; height: 255px; }
  .fp-2 { left: 25px; top: 301px; height: 257px; }
  .fp-4 { left: 250px; top: 310px; height: 248px; padding-top: 3px; }
  .content-panel .folio { left: 233px; top: 573px; }
</style>
</head>
<body>

<section class="page cover">
  <div class="brand">
    <span class="brand-mark"></span>
    <span class="brand-name">NEVB</span>
  </div>
  <p class="tagline">new thinking for better homes</p>

  <svg class="title-triangle" width="460" height="171" viewBox="0 0 460 171" aria-hidden="true">
    <polygon points="230,0 460,171 0,171" fill="var(--peach)"/>
  </svg>
  <h1 class="report-title">Is<br>Housing<br>Really Ready to Go<br>Digital? – A Manifesto for Change</h1>

  <p class="intro intro-1">The UK housing sector is stuck in a technology rut. Ubiquitous connectivity, machine learning and automation are transforming businesses across the economy, but social landlords remain wedded to systems and approaches which have successfully computerised the business practices of the 1960s and 1970s, but in too many areas have failed to move on.</p>
  <p class="intro intro-2">There is little evidence housing providers are capable of responding to the challenges and opportunities of a transformed digital world. At a time of rapidly falling budgets and the urgent need to reinvent business models, this represents a major unaddressed threat to the long term success of the sector.</p>

  <span class="folio">1</span>
</section>

<section class="page spread">
  <div class="brand">
    <span class="brand-mark"></span>
    <span class="brand-name">NEVB</span>
  </div>

  <svg class="section-banner" width="485" height="72" viewBox="0 0 485 72" aria-hidden="true">
    <polygon points="0,0 485,72 0,72" fill="var(--salmon)"/>
  </svg>
  <h2 class="section-heading">Five Big Failure Points</h2>
  <p class="section-lede">There are five big failure points in UK housing's approach to technology</p>

  <div class="content-panel">
    <p class="failure-point fp-1">1- the barriers to change are too high and opportunities to innovate too few – there are few examples of housing providers being willing to practically explore radical approaches to managing their stock outside of conventional “housing management system-driven” paradigms, and where change is attempted, the focus tends to be towards making existing systems work slightly better (often by layering on yet more sub-optimal solutions), rather than reinventing them from scratch. In other words, the disruption becoming commonplace across the wider digital economy is entirely missing from the housing sector. Housing Board and Exec teams are seeking safety in speeding up delivery of digital strategies that embed</p>
    <p class="failure-point fp-3">3- the barriers to change are too high and opportunities to innovate too few – there are few examples of housing providers being willing to practically explore radical approaches to managing their stock outside of conventional “housing management system-driven” paradigms, and where change is attempted, the focus tends to be towards making existing systems work slightly better (often by layering on yet more sub-optimal solutions), rather than reinventing them from scratch. In other words, the disruption becoming commonplace across the wider digital economy is entirely missing from the housing sector. Housing Board and Exec teams are seeking safety in speeding up delivery of digital strategies that embed</p>
    <p class="failure-point fp-2">2- the barriers to change are too high and opportunities to innovate too few – there are few examples of housing providers being willing to practically explore radical approaches to managing their stock outside of conventional “housing management system-driven” paradigms, and where change is attempted, the focus tends to be towards making existing systems work slightly better (often by layering on yet more sub-optimal solutions), rather than reinventing them from scratch. In other words, the disruption becoming commonplace across the wider digital economy is entirely missing from the housing sector. Housing Board and Exec teams are seeking safety in speeding up delivery of digital strategies that embed</p>
    <p class="failure-point fp-4">4- there is little or no understanding of technology issues on boards and senior teams – driving the perception that technology is an area of risk and cost rather than opportunity. Lack of internal knowledge leads to a inadequate understanding of opportunities and problems; an over-reliance on expensive consultant-driven solutions, often pushing major change or integration programmes that business are unable either to fully understand or risk assess; a lack of organisational ambition or confidence in internally assessing the performance of existing technology investment; and a lack of appreciation of the potential of new solutions and approaches that might be out there.</p>
    <span class="folio">2</span>
  </div>
</section>

</body>
</html>
```